Business Card Design

I am a realtor and i also flip houses. I am CEO and Founder of my business which is Halvorsen Group LLC which is named after my great uncle who died and i was really close to. He was a wonderful friendly man so i want my business to represent him too. My business works with a lot of different people but i want mainly something to show i am a strong confidant woman who owns there own business. I have a really fun personality so i don't want anything TOO serious or manly. I want the perfect mix. My last two business cards i created are too embarrassing to hand out because they are far too girly and i deal with a lot of millionaire clients. I live out in the Palm Springs California area. I think its very important to show i am a single mom, female with her own business at only 24. I don't want to just be a female that blends in with all of the other serious people but yet i don't want to seem immature. People are telling me to stay away from pinks and purples but i don't want blues and greens because they represent men more. But i won't say no to them if there is a happy medium.

Industry/Entity Type

Realtor

Contact Information for Business Card

Halvorsen Group, LLC
Corinne Pell
27318 Quillan Ave, B1 582
Rancho Mirage, CA 92270
760-555-0147
Corinnetpell@mailverta.com

```html
<!DOCTYPE html>
<html lang="en">
<head>
<meta charset="UTF-8">
<title>Halvorsen Group, LLC – Business Card</title>
<link rel="stylesheet" href="https://fonts.googleapis.com/css2?family=Didact+Gothic&family=Open+Sans:wght@400;600&display=swap">
<style>
  :root {
    --backdrop: #e9e6e2;
    --card-frame: #0b0b0b;
    --card-red: #c8333b;
    --card-red-light: #dc4a50;
    --card-red-dark: #bb2a33;
    --ink-light: #ffffff;
    --logo-cream: #f4ecd6;
  }
  * { box-sizing: border-box; margin: 0; padding: 0; }
  html, body {
    width: 1200px;
    height: 1000px;
    overflow: hidden;
    background: var(--backdrop);
  }
  .canvas {
    position: relative;
    width: 1200px;
    height: 1000px;
    display: flex;
    align-items: center;
    justify-content: center;
  }
  .business-card {
    width: 1000px;
    height: 580px;
    background: var(--card-frame);
    padding: 34px;
    box-shadow: 0 18px 40px rgba(0,0,0,0.25);
  }
  .card-face {
    position: relative;
    width: 100%;
    height: 100%;
    background:
      radial-gradient(ellipse at 48% 55%, var(--card-red-light) 0%, var(--card-red) 45%, var(--card-red-dark) 100%);
    color: var(--ink-light);
    font-family: "Open Sans", sans-serif;
  }
  .owner {
    position: absolute;
    top: 30px;
    right: 44px;
    text-align: center;
  }
  .owner-name {
    font-size: 30px;
    font-weight: 400;
    letter-spacing: 0.5px;
  }
  .owner-title {
    font-size: 21px;
    font-weight: 400;
    margin-top: 4px;
  }
  .brand {
    position: absolute;
    top: 48px;
    left: 0;
    width: 94%;
    display: flex;
    flex-direction: column;
    align-items: center;
  }
  .brand-dot {
    width: 82px;
    height: 82px;
    border-radius: 50%;
    background: var(--logo-cream);
  }
  .brand-name {
    margin-top: 14px;
    font-family: "Didact Gothic", sans-serif;
    font-size: 42px;
    font-weight: 400;
    color: var(--logo-cream);
    letter-spacing: 0.5px;
  }
  .contact {
    position: absolute;
    top: 296px;
    left: 56px;
    right: 30px;
    display: flex;
    align-items: stretch;
  }
  .address {
    font-size: 31px;
    line-height: 42px;
    letter-spacing: 0.5px;
    width: 420px;
  }
  .divider {
    width: 2px;
    background: var(--ink-light);
    margin: 0 22px 0 0;
    height: 150px;
  }
  .reach {
    font-size: 29px;
    line-height: 44px;
    letter-spacing: 0.5px;
    padding-top: 22px;
  }
</style>
</head>
<body>
  <main class="canvas">
    <article class="business-card">
      <div class="card-face">
        <header class="owner">
          <p class="owner-name">Corinne Pell</p>
          <p class="owner-title">CEO and Founder</p>
        </header>

        <div class="brand">
          <div class="brand-dot" aria-hidden="true"></div>
          <h1 class="brand-name">Halvorsen Group, LLC</h1>
        </div>

        <section class="contact">
          <address class="address">
            27318 Quillan Ave<br>
            B1 582 Rancho Mirage<br>
            CA 92270
          </address>
          <span class="divider" aria-hidden="true"></span>
          <div class="reach">
            <p class="phone">760-555-0147</p>
            <p class="email">Corinnetpell@mailverta.com</p>
          </div>
        </section>
      </div>
    </article>
  </main>
</body>
</html>
```